Double sided flyer for industrial investment firm

We need a A4 double sided flyer (1 page, see attached draft), which we will fold in the midle. Text is attached. What is missing is a professional and clean looking design. Text length can not be changed. it is all in German, but that should not influence the design. The flyer is added to a letter which we send to small industrial companies as an introduction to us as an investor.

What is important?
- No fancy, colorful and funny designs.
- We want a clean, professional almost minimalist design. it does not take much design elements.
- Format either landscape or vertical, whatever works best.
- stay with the colors of our company (grey, blue). see www.velmora-ag.ch for details.
- Currently used graphic in the document should be used, but is not a must. Otherwise stay with pictures or Swiss Alps (if more pictures are needed). will upload some pictures as examples.

Format for the finished flyer: InDesign and Word document or similar.
Updates

The flyer will be folded in the middle so that it becomes A5. all current designs work only as a A4 format. An A4 folded has basically 4 pages, each being A5 size. Please adapt the design accordingly.

Target Market(s)

Owners of small to medium industrial companies in Switzerland

Industry/Entity Type

Industrial

Font styles to use
Serif
Sans Serif

Colors
0255a3
3276b5
85abd2
cedeed

Requirements
Must have
• 1 page, double sided. folded in the middle. A4 Format

```html
<!DOCTYPE html>
<html lang="de">
<head>
<meta charset="utf-8">
<title>Fragen und Antworten zu Velmora</title>
<link href="https://fonts.googleapis.com/css2?family=PT+Sans:wght@400;700&display=swap" rel="stylesheet">
<style>
  :root {
    --navy: #0d2a6b;
    --brand-blue: #0255a3;
    --mid-blue: #3276b5;
    --light-blue: #85abd2;
    --pale-blue: #cedeed;
    --heading: #1b3d7c;
    --band-blue: #24448f;
    --band-grey: #9a9a9a;
    --text: #5e5e5e;
    --white: #ffffff;
  }
  * { box-sizing: border-box; margin: 0; padding: 0; }
  html, body { width: 927px; height: 1200px; overflow: hidden; background: var(--white); }
  .flyer {
    position: relative; width: 927px; height: 1200px; overflow: hidden;
    font-family: "PT Sans", sans-serif; color: var(--text);
    hyphens: auto; -webkit-hyphens: auto;
  }

  .hero-photo {
    position: absolute; left: 0; top: 0; width: 927px; height: 490px;
    background: linear-gradient(180deg, #0a1a4f 0%, #253a82 42%, #c9d3e8 72%, #6a78a6 100%);
  }
  .hero-band { position: absolute; left: 0; top: 490px; width: 927px; height: 92px; background: var(--band-blue); }
  .hero-rule { position: absolute; left: 0; top: 582px; width: 927px; height: 22px; background: var(--band-grey); }

  .brand-tab {
    position: absolute; left: 25px; top: 0; width: 320px; height: 80px;
    background: var(--white); border-radius: 0 0 10px 10px;
    display: flex; align-items: center; gap: 14px; padding-left: 26px;
  }
  .brand-mark { width: 24px; height: 24px; background: var(--heading); }
  .brand-name { font-weight: 700; font-size: 36px; color: var(--heading); letter-spacing: 1px; }

  .page-title {
    position: absolute; left: 362px; top: 42px;
    font-size: 34px; font-weight: 700; color: var(--white); letter-spacing: -0.5px;
  }
  .web-address {
    position: absolute; left: 90px; top: 104px;
    font-size: 16px; color: var(--white); letter-spacing: 3px;
  }

  .qa { position: absolute; left: 305px; top: 650px; width: 545px; height: 550px; overflow: hidden; }
  .qa h2 { font-size: 24px; font-weight: 700; color: var(--heading); margin-bottom: 18px; letter-spacing: -0.3px; line-height: 30px; }
  .qa p { font-size: 13.4px; line-height: 17px; text-align: justify; margin-bottom: 22px; }

  .about {
    position: absolute; left: 56px; top: 733px; width: 217px; height: 383px;
    border: 3px dotted var(--heading);
    border-radius: 0 22px 22px 0; padding: 22px 10px 0 12px;
  }
  .about h3 { font-size: 24px; font-weight: 400; color: var(--heading); margin-bottom: 26px; line-height: 28px; }
  .about p { font-size: 13.2px; line-height: 16.6px; text-align: justify; margin-bottom: 17px; }
</style>
</head>
<body>
<div class="flyer">
  <div class="hero-photo" role="img" aria-label="Photograph of a snow-covered Alpine peak under a deep blue sky"></div>
  <div class="hero-band"></div>
  <div class="hero-rule"></div>

  <div class="brand-tab"><span class="brand-mark"></span><span class="brand-name">VELMORA</span></div>
  <h1 class="page-title">Fragen und Antworten zu Velmora</h1>
  <div class="web-address">www.velmora-ag.ch</div>

  <aside class="about">
    <h3>Wer sind wir?</h3>
    <p>Wir sind eine Gruppe von ca. 15 Unternehmern, welche unser Kapital in mittelständische Industrieunternehmen investieren mit einem langfristigen Ansatz. Wir haben unser Kapital in der Velmora AG gebündelt und investieren nur in eine kleine Anzahl von Unternehmen.</p>
    <p>Alle unsere Investoren sind Schweizer mit Wohnsitz in der Schweiz. Wir sind kein Private Equity Fund mit einer definierten Haltedauer und einem Portfolio Ansatz.</p>
  </aside>

  <main class="qa">
    <h2>Was ist unser Ziel/Vision?</h2>
    <p>Das Ziel ist nicht Grösse sondern Qualität. Wir wollen eine kleine Industriegruppe aufbauen mit qualitativ hochwertigen Schweizer Industrieunternehmen, welche unabhängig voneinander operieren.</p>
    <h2>Welches Kapital investieren wir?</h2>
    <p>Wir investieren unser eigenes Kapital, welches wir über die Jahre aufgebaut haben. Anstatt dieses Kapital an der Börse oder in Immobilien anzulegen, kaufen wir gemeinsam ein Unternehmen und entwickeln dieses. Wir haben mehr Vertrauen in unsere Fähigkeit eine Firma zu entwickeln als in die Finanzmärkte. Einen Teil des Kaufpreises eines Unternehmens finanzieren wir jeweils mit einer Grossbank. Diesen Kredit zahlen wir in der Regel innert 3-4 Jahren zurück, da wir von Banken unabhängig sein wollen.</p>
    <h2>Wie arbeiten wir?</h2>
    <p>Wir sind keine Finanzinvestoren sondern Unternehmer. Der Unterschied liegt in dem intensiven Fokus den wir auf die wenigen Firmen legen, die wir besitzen. Wir wollen unsere Kunden und Märkte im Detail verstehen und so für das Management ein guter Diskussionspartner sein. Das bedingt, dass wir nur sehr wenige Firmen kaufen und diese dann über die Jahre ausbauen im Gegensatz zu einem Finanzinvestor, welcher sich an vielen Unternehmen beteiligt, um sein Risiko zu reduzieren und dann das Unternehmen wieder verkauft. Wir übernehmen operative Aufgaben und leiten gewisse Projekte, damit sich das Management noch besser auf das Tagesgeschäft konzentrieren kann. Diese Arbeiten werden aber immer in Abstimmung mit dem Management ausgeführt, damit</p>
  </main>
</div>
</body>
</html>
```